Business Card Design

I'm a commercial general contractor remodel offices, hotels, health clubs and stores mostly San Francisco and the peninsula
the file I down loaded is kind of what I want I like the I beam with my company name in it, that would be fine with me but if you have better Idea will look at it you never know, I'm decided to give in and change my company name to how every one knows me, I have been in business since 1991, I like the I beam logo I included one of my old card from my old company for reference for you.

Industry/Entity Type

Business

Contact Information for Business Card

BRAVO CONSTRUCTION (is my company name)
Reginald Pottle contractor, LIc 384217
4318 Quarry Lane, San Bruno, California 94066
mobile, (415) 555-0147
phone (650) 555-0183
Fax, (650) 555-0184
email, bravo@bravoconstruction.example

```html
<!DOCTYPE html>
<html lang="en">
<head>
<meta charset="utf-8">
<title>Bravo Construction – Business Card</title>
<link rel="stylesheet" href="https://fonts.googleapis.com/css2?family=Open+Sans:wght@300;400;600&display=swap">
<style>
  :root {
    --sky-light: #f4f4f4;
    --sky-mid: #dcdcdd;
    --sky-edge: #c4c5c7;
    --skyline-top: #cdcecf;
    --skyline-bottom: #b3b4b6;
    --band: #333333;
    --base: #a9aaae;
    --accent: #2b9ad6;
    --ink: #333333;
    --ink-soft: #444444;
    --band-text: #e4e4e4;
  }
  * { margin: 0; padding: 0; box-sizing: border-box; }
  html, body { width: 1200px; height: 702px; overflow: hidden; background: #ffffff; }
  .card {
    position: relative;
    width: 1200px;
    height: 702px;
    overflow: hidden;
    font-family: "Open Sans", Arial, sans-serif;
    background: radial-gradient(ellipse 70% 80% at 50% 35%, var(--sky-light) 0%, var(--sky-mid) 60%, var(--sky-edge) 100%);
  }
  .license {
    position: absolute;
    top: 52px;
    right: 58px;
    font-size: 30px;
    font-weight: 400;
    letter-spacing: 1px;
    color: var(--ink-soft);
  }
  .skyline {
    position: absolute;
    left: 0;
    top: 232px;
    width: 1200px;
    height: 146px;
    background: linear-gradient(to bottom, rgba(205,206,207,0.35) 0%, var(--skyline-top) 40%, var(--skyline-bottom) 100%);
  }
  .brand-mark {
    position: absolute;
    left: 0;
    top: 0;
    width: 1200px;
    height: 340px;
  }
  .brand-name {
    position: absolute;
    top: 112px;
    left: 0;
    width: 1200px;
    text-align: center;
    font-size: 140px;
    line-height: 1;
    font-weight: 600;
    letter-spacing: 8px;
    color: var(--ink);
  }
  .brand-sub {
    position: absolute;
    top: 274px;
    left: 0;
    width: 1200px;
    text-align: center;
    font-size: 44px;
    line-height: 1.2;
    font-weight: 600;
    letter-spacing: 6px;
    color: var(--ink);
  }
  .brand-square {
    position: absolute;
    left: 922px;
    top: 140px;
    width: 56px;
    height: 56px;
    background: var(--accent);
  }
  .name-band {
    position: absolute;
    left: 0;
    top: 378px;
    width: 1200px;
    height: 81px;
    background: var(--band);
    display: flex;
    align-items: center;
    padding-left: 102px;
  }
  .name-band .person {
    font-size: 44px;
    font-weight: 400;
    color: var(--accent);
    letter-spacing: 0.5px;
  }
  .name-band .role {
    font-size: 44px;
    font-weight: 300;
    color: var(--band-text);
    margin-left: 38px;
    letter-spacing: 0.5px;
  }
  .contact-area {
    position: absolute;
    left: 0;
    top: 459px;
    width: 1200px;
    height: 243px;
    background: var(--base);
  }
  .contact {
    position: absolute;
    display: flex;
    align-items: center;
    color: var(--ink);
  }
  .contact svg { position: absolute; }
  .phones .contact { font-size: 32px; font-weight: 400; letter-spacing: 0.5px; }
  .online .contact { font-size: 26px; font-weight: 400; }
  .icon { fill: none; stroke: var(--accent); stroke-width: 2.4; }
  .icon-fill { fill: var(--accent); }
</style>
</head>
<body>
<div class="card">
  <div class="license">LIC 384217</div>

  <div class="skyline" role="img" aria-label="Grey silhouette of the San Francisco skyline with a suspension bridge on the left"></div>

  <div class="brand-mark">
    <div class="brand-name">BRAVO</div>
    <div class="brand-square"></div>
    <div class="brand-sub">CONSTRUCTION</div>
  </div>

  <div class="name-band">
    <span class="person">REGINALD POTTLE</span>
    <span class="role">CONTRACTOR</span>
  </div>

  <div class="contact-area">
    <div class="phones">
      <div class="contact" style="left:96px; top:28px; height:40px;">
        <svg width="42" height="42" viewBox="0 0 42 42" style="left:0; top:-2px;">
          <rect class="icon-fill" x="12" y="2" width="20" height="34" rx="3"/>
          <rect x="15" y="7" width="14" height="22" fill="#a9aaae"/>
          <path class="icon-fill" d="M4 18 h10 v20 h-6 a4 4 0 0 1 -4 -4 z"/>
        </svg>
        <span style="margin-left:86px;">(415) 555-0147</span>
      </div>
      <div class="contact" style="left:96px; top:80px; height:40px;">
        <svg width="42" height="42" viewBox="0 0 42 42" style="left:0; top:-1px;">
          <circle class="icon" cx="21" cy="21" r="18"/>
          <path class="icon-fill" d="M14 11 l4 -1 l3 6 l-3 2 q2 5 6 7 l2 -3 l6 3 l-1 4 q-4 3 -10 -1 q-6 -4 -8 -10 q-1 -5 1 -7 z"/>
        </svg>
        <span style="margin-left:86px;">(650) 555-0183</span>
      </div>
      <div class="contact" style="left:96px; top:137px; height:40px;">
        <svg width="42" height="42" viewBox="0 0 42 42" style="left:0; top:-1px;">
          <rect class="icon" x="8" y="4" width="26" height="34" rx="2"/>
          <line class="icon" x1="13" y1="11" x2="29" y2="11"/>
          <line class="icon" x1="13" y1="17" x2="29" y2="17"/>
          <rect class="icon-fill" x="12" y="26" width="18" height="8"/>
        </svg>
        <span style="margin-left:86px;">(650) 555-0184</span>
      </div>
    </div>

    <div class="online">
      <div class="contact" style="left:616px; top:20px; height:40px;">
        <svg width="42" height="42" viewBox="0 0 42 42" style="left:0; top:-1px;">
          <circle class="icon" cx="21" cy="21" r="18"/>
          <rect class="icon" x="11" y="14" width="20" height="14"/>
          <polyline class="icon" points="11,14 21,22 31,14"/>
        </svg>
        <span style="margin-left:80px;">bravo@bravoconstruction.example</span>
      </div>
      <div class="contact" style="left:616px; top:68px; height:84px; align-items:flex-start;">
        <svg width="42" height="42" viewBox="0 0 42 42" style="left:0; top:22px;">
          <path class="icon" d="M21 39 q-12 -14 -12 -22 a12 12 0 0 1 24 0 q0 8 -12 22 z"/>
          <circle class="icon" cx="21" cy="17" r="4.5"/>
        </svg>
        <span style="margin-left:80px; line-height:42px;">4318 Quarry Lane, San Bruno<br>California 94066</span>
      </div>
      <div class="contact" style="left:616px; top:153px; height:40px;">
        <svg width="42" height="42" viewBox="0 0 42 42" style="left:0; top:-1px;">
          <circle class="icon" cx="21" cy="21" r="16"/>
          <ellipse class="icon" cx="21" cy="21" rx="7" ry="16"/>
          <line class="icon" x1="5" y1="21" x2="37" y2="21"/>
          <line class="icon" x1="8" y1="13" x2="34" y2="13"/>
          <line class="icon" x1="8" y1="29" x2="34" y2="29"/>
        </svg>
        <span style="margin-left:80px;">www.bravoconstruction.example</span>
      </div>
    </div>
  </div>
</div>
</body>
</html>
```